Lotus Bowl take out menu

We need a take out menu design using our menu attached. Info to include would be our address: 5817 Meridel Harrow Pkwy #204, Lafayette, LA 70508. Phone number is 337-614-2953. website is www.lotusbowlvtr.example.

Industry/Entity Type

Asian Restaurant

```html
<!DOCTYPE html>
<html lang="en">
<head>
<meta charset="utf-8">
<title>Lotus Bowl – Take Out Menu</title>
<link rel="stylesheet" href="https://fonts.googleapis.com/css2?family=Bangers&family=Cinzel:wght@700&family=Lato:wght@400;700;900&display=swap">
<style>
  :root {
    --red: #e01b22;
    --black: #111111;
    --ink: #2a2a2a;
    --paper: #ffffff;
    --backdrop: #4a4a4a;
    --leader: #9a9a9a;
  }
  * { box-sizing: border-box; margin: 0; padding: 0; }
  html, body { width: 1200px; height: 900px; overflow: hidden; }
  body { background: var(--backdrop); font-family: "Lato", sans-serif; color: var(--ink); position: relative; }

  .page { position: absolute; top: 150px; width: 375px; height: 600px; background: var(--paper); overflow: hidden; }
  .cover { left: 30px; }
  .appetizers-page { left: 425px; }
  .entrees-page { left: 800px; box-shadow: inset 8px 0 10px -8px rgba(0,0,0,.25); }
  .page-art { position: absolute; inset: 0; width: 375px; height: 600px; }

  /* cover */
  .brand-block { position: absolute; left: 0; right: 0; top: 395px; text-align: center; }
  .brand-name { font-family: "Cinzel", serif; font-weight: 700; font-size: 38px; color: var(--black); letter-spacing: 1px; line-height: 1; }
  .brand-tagline { font-family: "Cinzel", serif; font-weight: 700; font-size: 11px; letter-spacing: 4px; color: var(--black); margin-top: 8px; }
  .brand-contact { font-family: "Lato", sans-serif; font-size: 8.5px; color: var(--red); margin-top: 14px; line-height: 1.5; }

  /* inside pages */
  .section-title { position: absolute; left: 32px; font-family: "Bangers", sans-serif; color: var(--red); font-size: 38px; letter-spacing: 1px; line-height: 1; }
  .appetizers-page .section-title { top: 125px; }
  .entrees-page .section-title { top: 140px; }

  .menu-col { position: absolute; width: 150px; }
  .col-left { left: 32px; }
  .col-right { left: 194px; }
  .item { margin-bottom: 8px; }
  .item-head { display: flex; align-items: baseline; gap: 3px; }
  .item-name { font-weight: 900; font-size: 8.5px; color: var(--black); min-width: 0; }
  .leader { flex: 1; min-width: 8px; border-bottom: 1px dotted var(--leader); transform: translateY(-2px); }
  .item-price { font-weight: 700; font-size: 8.5px; color: var(--black); flex-shrink: 0; }
  .item-desc { font-size: 6.8px; line-height: 1.3; color: var(--ink); margin-top: 1px; }

  .appetizers-page .menu-col { top: 175px; }
  .entrees-page .col-left { top: 190px; }
  .entrees-page .col-right { top: 190px; }
  .entrees-page .item { margin-bottom: 11px; }

  .category-band { background: var(--black); color: var(--paper); font-size: 7px; font-weight: 700; letter-spacing: 1px; text-align: center; padding: 3px 0; border-radius: 8px; margin: 2px 0 9px; text-transform: uppercase; }
</style>
</head>
<body>

<!-- Front cover -->
<section class="page cover">
  <svg class="page-art" viewBox="0 0 375 600">
    <defs>
      <radialGradient id="dishGreen" cx="50%" cy="45%" r="60%">
        <stop offset="0%" stop-color="#7a5a3e"/><stop offset="55%" stop-color="#4f7a2e"/><stop offset="100%" stop-color="#e8e8e4"/>
      </radialGradient>
      <radialGradient id="dishRed" cx="50%" cy="45%" r="60%">
        <stop offset="0%" stop-color="#c8432c"/><stop offset="55%" stop-color="#8aa640"/><stop offset="100%" stop-color="#f1d6cf"/>
      </radialGradient>
      <radialGradient id="dishGold" cx="50%" cy="45%" r="60%">
        <stop offset="0%" stop-color="#b5652e"/><stop offset="60%" stop-color="#d9a35a"/><stop offset="100%" stop-color="#5c6f86"/>
      </radialGradient>
      <radialGradient id="dishPale" cx="50%" cy="45%" r="60%">
        <stop offset="0%" stop-color="#f2efe6"/><stop offset="55%" stop-color="#d98aa8"/><stop offset="100%" stop-color="#9c9a94"/>
      </radialGradient>
    </defs>
    <rect x="22" y="60" width="331" height="518" fill="none" stroke="var(--red)" stroke-width="2"/>
    <rect x="0" y="0" width="375" height="160" fill="var(--red)"/>
    <circle cx="110" cy="150" r="118" fill="var(--red)"/>
    <circle cx="275" cy="140" r="118" fill="var(--red)"/>
    <circle cx="118" cy="150" r="96" fill="var(--black)"/>
    <circle cx="280" cy="140" r="96" fill="var(--black)"/>
    <circle cx="112" cy="145" r="86" fill="url(#dishGreen)" role="img" aria-label="Photo of stir-fried beef with snow peas and mushrooms"/>
    <circle cx="286" cy="136" r="86" fill="url(#dishRed)" role="img" aria-label="Photo of a spicy vegetable and seafood salad"/>
  </svg>
  <div class="brand-block">
    <h1 class="brand-name">LOTUS BOWL</h1>
    <p class="brand-tagline">FRESH ASIAN CUISINE</p>
    <p class="brand-contact">5817 Meridel Harrow Pkwy #204, Lafayette, LA 70508<br>Ph: 337-614-2953 | www.lotusbowlvtr.example</p>
  </div>
</section>

<!-- Inside left: appetizers -->
<section class="page appetizers-page">
  <svg class="page-art" viewBox="0 0 375 600">
    <rect x="20" y="40" width="335" height="540" fill="none" stroke="var(--red)" stroke-width="2"/>
    <circle cx="78" cy="72" r="38" fill="var(--red)"/>
    <circle cx="78" cy="72" r="29" fill="var(--black)"/>
    <circle cx="290" cy="100" r="64" fill="var(--red)"/>
    <circle cx="290" cy="100" r="53" fill="var(--black)"/>
    <circle cx="290" cy="100" r="46" fill="url(#dishGold)" role="img" aria-label="Photo of grilled skewers and crispy bao buns"/>
  </svg>
  <h2 class="section-title">APPETIZERS</h2>

  <div class="menu-col col-left">
    <div class="item"><div class="item-head"><span class="item-name">Edamame</span><span class="leader"></span><span class="item-price">$4</span></div><p class="item-desc">Seasoned &amp; boiled soy bean</p></div>
    <div class="item"><div class="item-head"><span class="item-name">Scallion Pancakes</span><span class="leader"></span><span class="item-price">$6</span></div><p class="item-desc">Traditional Chinese flatbread folded with oil and minced scallions and pan fried</p></div>
    <div class="item"><div class="item-head"><span class="item-name">Lotus Bowl Lettuce Wraps</span><span class="leader"></span><span class="item-price">$8</span></div><p class="item-desc">Seasoned ground chicken drizzled with our top secret homemade sauce served with lettuce wraps</p></div>
    <div class="item"><div class="item-head"><span class="item-name">Buddha Bang Shrimp</span><span class="leader"></span><span class="item-price">$9</span></div><p class="item-desc">Crispy fried shrimp tossed in our creamy spicy sauce</p></div>
    <div class="item"><div class="item-head"><span class="item-name">Drunken Chicken</span><span class="leader"></span><span class="item-price">$8</span></div><p class="item-desc">Chicken, Thai chili in a house made spicy sauce</p></div>
    <div class="item"><div class="item-head"><span class="item-name">Sichuan Spiced Beef</span><span class="leader"></span><span class="item-price">$9</span></div><p class="item-desc">Beef Shank, beef tripe, cilantro, peanuts and celery</p></div>
    <div class="item"><div class="item-head"><span class="item-name">Beef Crispy Bottom Bao</span><span class="leader"></span><span class="item-price">$10</span></div><p class="item-desc">Pan fried crispy bottom Bao stuffed with beef, drizzled with scallion and sesame (Fresh made to order, takes at least 20 mins to serve)</p></div>
    <div class="item"><div class="item-head"><span class="item-name">Shrimp &amp; Beef Crispy Bao</span><span class="leader"></span><span class="item-price">$10</span></div><p class="item-desc">Pan fried crispy bottom Bao stuffed with beef and shrimp, drizzled with scallion and sesame (Fresh made to order, takes at least 20 mins to serve)</p></div>
  </div>

  <div class="menu-col col-right">
    <div class="item"><div class="item-head"><span class="item-name">Salt &amp; Pepper Calamari</span><span class="leader"></span><span class="item-price">$9</span></div><p class="item-desc">Crispy Calamari with Green &amp; red peppers and onions</p></div>
    <div class="item"><div class="item-head"><span class="item-name">Crispy Mala Beef Jerky</span><span class="leader"></span><span class="item-price">$9</span></div><p class="item-desc">Dry fried shredded beef with various peppers in sesame and peppercorn oil</p></div>
    <div class="item"><div class="item-head"><span class="item-name">Fried Chicken Dumplings (6)</span><span class="leader"></span><span class="item-price">$6</span></div><p class="item-desc">Chinese dumplings stuffed with Chicken, Shiitake mushrooms and bamboo shoots</p></div>
    <div class="item"><div class="item-head"><span class="item-name">Red Oil Dumplings (6)</span><span class="leader"></span><span class="item-price">$7</span></div><p class="item-desc">Pork filled dumplings in Sichuan red oil sauce drizzled with sesame</p></div>
    <div class="item"><div class="item-head"><span class="item-name">Pork Egg Rolls (2)</span><span class="leader"></span><span class="item-price">$4</span></div><p class="item-desc">Hand rolled with julienned veggies with our sweet n' sour mustard sauce</p></div>
    <div class="item"><div class="item-head"><span class="item-name">Vegetarian Spring Rolls (3)</span><span class="leader"></span><span class="item-price">$4</span></div><p class="item-desc">Traditional Asian Roll served with a sweet chili sauce</p></div>
    <div class="item"><div class="item-head"><span class="item-name">Garlic Cucumber Salad</span><span class="leader"></span><span class="item-price">$7</span></div><p class="item-desc">Sliced cucumber with a garlic vinaigrette</p></div>
    <div class="item"><div class="item-head"><span class="item-name">Hot n' Sour Soup</span><span class="leader"></span><span class="item-price">$4</span></div><p class="item-desc">Tangy broth with Bamboo shoot, wood ear fungus, tofu, egg and carrots</p></div>
    <div class="item"><div class="item-head"><span class="item-name">West Lake Soup</span><span class="leader"></span><span class="item-price">$4</span></div><p class="item-desc">Light creamy soup with ground beef, diced Shiitake mushroom, tofu, bamboo shoots, egg white and cilantro</p></div>
  </div>
</section>

<!-- Inside right: entrees -->
<section class="page entrees-page">
  <svg class="page-art" viewBox="0 0 375 600">
    <rect x="20" y="40" width="335" height="540" fill="none" stroke="var(--red)" stroke-width="2"/>
    <circle cx="78" cy="88" r="38" fill="var(--red)"/>
    <circle cx="78" cy="88" r="29" fill="var(--black)"/>
    <circle cx="222" cy="95" r="60" fill="var(--red)"/>
    <circle cx="306" cy="88" r="60" fill="var(--red)"/>
    <circle cx="222" cy="95" r="50" fill="var(--black)"/>
    <circle cx="306" cy="88" r="50" fill="var(--black)"/>
    <circle cx="222" cy="95" r="43" fill="url(#dishPale)" role="img" aria-label="Photo of scallops plated on a pink garnish"/>
    <circle cx="308" cy="88" r="43" fill="url(#dishGold)" role="img" aria-label="Photo of glazed roast duck legs"/>
  </svg>
  <h2 class="section-title">ENTREES</h2>

  <div class="menu-col col-left">
    <div class="item"><div class="item-head"><span class="item-name">Jasmine Tea Smoked Duck</span><span class="leader"></span><span class="item-price">$24</span></div><p class="item-desc">Boneless half duck served with thinly sliced cucumber, scallion, house made duck sauce and soft flour wrap</p></div>
    <div class="item"><div class="item-head"><span class="item-name">Sizzling Cumin Lamb</span><span class="leader"></span><span class="item-price">$16</span></div><p class="item-desc">Tender pieces of lamb rubbed in cumin, Sichuan peppers, celery and cilantro</p></div>
    <div class="item"><div class="item-head"><span class="item-name">Chef Lin's Spicy Beef</span><span class="leader"></span><span class="item-price">$16</span></div><p class="item-desc">Angus beef in house made green peppercorn sauce, drizzled with fresh Sichuan peppercorn, Thai chili and cilantro</p></div>
    <div class="item"><div class="item-head"><span class="item-name">Dancing Beef</span><span class="leader"></span><span class="item-price">$16</span></div><p class="item-desc">Angus Beef slices on a bed of sizzling rice crackers, black peppercorn and Thai chili</p></div>
    <div class="item"><div class="item-head"><span class="item-name">Oyster Beef</span><span class="leader"></span><span class="item-price">$14</span></div><p class="item-desc">Tender cuts of steak wok fried and marinated in a homemade oyster sauce</p></div>
    <div class="item"><div class="item-head"><span class="item-name">Double Pepper Beef</span><span class="leader"></span><span class="item-price">$16</span></div><p class="item-desc">Angus Steak cubes with fresh green peppercorn, Thai chili, Serrano Pepper and celery</p></div>
    <div class="item"><div class="item-head"><span class="item-name">Black Pepper Steak</span><span class="leader"></span><span class="item-price">$15</span></div><p class="item-desc">Tender cuts of steak mixed with onions and red and green bell peppers</p></div>
  </div>

  <div class="menu-col col-right">
    <p class="category-band">Chef Specialties</p>
    <div class="item"><div class="item-head"><span class="item-name">Chef Lin's Spicy Fish</span><span class="leader"></span><span class="item-price">$17</span></div><p class="item-desc">Fish filet in house made green peppercorn sauce, drizzled with fresh Sichuan peppercorn, Thai chili and cilantro</p></div>
    <div class="item"><div class="item-head"><span class="item-name">General Tso's Scallops</span><span class="leader"></span><span class="item-price">$18</span></div><p class="item-desc">The perfect combination of tender scallops marinated in a sweet chili sauce with broccoli and red peppers</p></div>
    <p class="category-band">Beef &amp; Pork</p>
    <div class="item"><div class="item-head"><span class="item-name">Singapore Baby Back Ribs</span><span class="leader"></span><span class="item-price">$16</span></div><p class="item-desc">Tender Baby back ribs rubbed in a Thai inspired sweet tangy glaze</p></div>
    <div class="item"><div class="item-head"><span class="item-name">Dancing Pork Belly</span><span class="leader"></span><span class="item-price">$15</span></div><p class="item-desc">Braised Pork Belly on sizzling rice cracker</p></div>
    <div class="item"><div class="item-head"><span class="item-name">Twice Cooked Pork</span><span class="leader"></span><span class="item-price">$14</span></div><p class="item-desc">Stir fried Pork Belly slices with leek and fermented black beans</p></div>
  </div>
</section>

</body>
</html>
```